Ductless Mini Split Business Website

Amber Kite Services is looking to design an eye catching educational website about installing Ductless mini splits.

Similar to this company.
https://www.cedarcoolair.com/

```html
<!DOCTYPE html>
<html lang="en">
<head>
<meta charset="utf-8">
<title>Amber Kite Services – Ductless Experts</title>
<link href="https://fonts.googleapis.com/css2?family=Poppins:wght@400;500;600;700;800&family=Open+Sans:wght@400;600;700&display=swap" rel="stylesheet">
<style>
:root{
  --yellow:#f9c80e;
  --yellow-dark:#e2b300;
  --ink:#1b1b1b;
  --dark:#222325;
  --darker:#161718;
  --grey:#6d6d6d;
  --light:#f4f4f4;
  --line:#e3e3e3;
  --white:#ffffff;
}
*{box-sizing:border-box;margin:0;padding:0}
html,body{width:1200px;height:3724px;overflow:hidden}
body{position:relative;background:var(--white);font-family:"Open Sans",Arial,sans-serif;color:var(--ink);font-size:11px;line-height:1.6}
section,header,footer,nav{position:absolute;left:0;width:1200px}
h1,h2,h3,h4{font-family:"Poppins",Arial,sans-serif}
.btn{display:inline-block;background:var(--yellow);color:var(--ink);font-family:"Poppins",sans-serif;font-weight:700;font-size:10px;letter-spacing:.5px;padding:9px 22px;border-radius:20px;text-transform:uppercase}
.ph{position:absolute}
.brand{display:flex;align-items:center;gap:8px}
.brand .mark{width:34px;height:34px;background:var(--yellow);border-radius:50%}
.brand .name{font-family:"Poppins",sans-serif;font-weight:800;font-size:18px;line-height:1.05;color:var(--ink)}
.section-icon{width:26px;height:26px;border-radius:50%;background:var(--yellow);margin:0 auto 8px}
.section-title{font-size:26px;font-weight:700;text-align:center}

.topbar{position:absolute;left:0;width:1200px;top:0;height:24px;background:var(--yellow);font-size:9px;display:flex;justify-content:space-between;align-items:center;padding:0 232px;font-weight:600}
.topbar .info{display:flex;gap:18px}
.site-header{top:24px;height:88px;display:flex;align-items:center;justify-content:space-between;padding:0 232px}
.site-header .brand-block .sub{font-family:"Poppins",sans-serif;font-size:11px;font-weight:700;letter-spacing:1px;margin-top:2px;color:var(--ink)}
.header-right{display:flex;align-items:center;gap:24px}
.call{display:flex;align-items:center;gap:8px}
.call small{display:block;font-size:9px;color:var(--grey)}
.call strong{font-family:"Poppins",sans-serif;font-size:15px;color:var(--yellow-dark)}
.main-nav{top:112px;height:32px;background:var(--white);border-top:1px solid var(--line);display:flex;justify-content:center}
.main-nav a{font-family:"Poppins",sans-serif;font-size:9px;font-weight:600;padding:0 20px;line-height:32px;color:var(--ink);text-decoration:none}
.main-nav a.active{background:var(--yellow)}
.hero{top:144px;height:386px;overflow:hidden}
.hero .photo{left:0;top:0;width:1200px;height:386px;background:linear-gradient(90deg,#cfcac3 0%,#8a8580 45%,#3d3c3b 75%,#2a2a2a 100%)}
.hero .copy{position:absolute;left:700px;top:120px;color:var(--white)}
.hero .copy em{font-style:italic;font-size:12px}
.hero h1{font-size:38px;line-height:1.12;font-weight:700;margin:6px 0 18px;width:380px}
.hero .arrow{position:absolute;top:178px;width:26px;height:26px;border-radius:50%;background:rgba(255,255,255,.35)}
.about{top:530px;height:630px;background:#fafafa}
.about .photo{left:232px;top:250px;width:360px;height:380px;background:linear-gradient(135deg,#b9c6cf,#6f7e88)}
.about .badge{position:absolute;left:352px;top:330px;width:250px;height:200px;background:var(--yellow);padding:22px}
.about .badge .art{position:absolute;right:16px;top:-30px;width:80px;height:80px;border-radius:50%;background:#e8e0c8}
.about .badge h3{font-size:20px;line-height:1.1;font-weight:700}
.about .badge p.sub{font-size:10px;font-weight:600}
.about .badge .play{display:flex;align-items:center;gap:10px;margin-top:40px;font-weight:700;font-size:10px;line-height:1.3}
.about .badge .play span.c{width:34px;height:34px;border-radius:50%;background:var(--ink);display:flex;align-items:center;justify-content:center}
.about .text{position:absolute;left:620px;top:70px;width:380px;color:var(--grey);font-size:10.5px}
.about .text p{margin-bottom:12px}
.about .text h2{font-size:22px;color:var(--ink);margin:14px 0 12px;font-weight:700}
.services{top:1160px;height:640px;padding-top:66px}
.grid{position:absolute;left:232px;top:160px;width:736px;display:grid;grid-template-columns:repeat(4,175px);gap:20px 12px}
.card{height:140px;background:var(--white);box-shadow:0 2px 6px rgba(0,0,0,.12)}
.card .img{height:104px;background:linear-gradient(135deg,#d9dde0,#9aa3a8)}
.card .label{height:36px;background:var(--yellow);font-family:"Poppins",sans-serif;font-size:8.5px;font-weight:700;text-align:center;display:flex;align-items:center;justify-content:center;padding:0 10px;line-height:1.2;text-transform:uppercase}
.services .btn{position:absolute;left:522px;top:530px}
.contact{top:1800px;height:600px;background:linear-gradient(90deg,#2b2b2c,#3a3b3c 50%,#2b2b2c);color:var(--white);text-align:center;padding-top:80px}
.contact h2{font-size:26px;font-weight:700;line-height:1.3}
.contact .lead{font-size:13px;margin-top:6px;font-weight:600}
.contact .lead2{font-size:15px;font-family:"Poppins",sans-serif;font-weight:600}
.contact .lead2 b{color:var(--yellow)}
.form{position:absolute;left:415px;top:250px;width:370px;display:grid;grid-template-columns:1fr 1fr;gap:12px}
.field{height:28px;background:var(--white);color:#888;font-size:9px;text-align:left;padding:7px 10px;line-height:1.5}
.field.full{grid-column:1/3}
.field.msg{height:80px}
.contact .btn{position:absolute;left:540px;top:520px}
.reviews{top:2400px;height:480px;background:var(--light);overflow:hidden}
.reviews .photo{left:900px;top:60px;width:300px;height:420px;background:linear-gradient(180deg,#e9e9e9,#bdbdbd)}
.reviews .head{position:absolute;left:232px;top:110px;width:668px;text-align:center}
.rv{position:absolute;top:205px;width:210px}
.rv .box{background:var(--white);padding:16px;font-size:9px;color:var(--grey);height:110px;box-shadow:0 1px 4px rgba(0,0,0,.08)}
.rv .stars{color:var(--yellow-dark);letter-spacing:2px;margin-top:6px;font-size:10px}
.rv .who{display:flex;justify-content:flex-end;align-items:center;gap:8px;margin-top:12px;font-weight:700;font-size:9px}
.rv .who span.av{width:28px;height:28px;border-radius:50%;background:#b0b0b0}
.dots{position:absolute;left:540px;top:400px;display:flex;gap:5px}
.dots i{width:6px;height:6px;border-radius:50%;background:#c9c9c9}
.dots i.on{background:var(--yellow-dark)}
.faq-blog{top:2880px;height:560px;background:linear-gradient(180deg,#fff 70%,#e9e9e9)}
.faq{position:absolute;left:232px;top:50px;width:350px}
.faq h3,.blog h3{font-size:20px;font-weight:700;margin-bottom:16px}
.q{border:1px solid var(--line);background:var(--white);padding:9px 30px 9px 12px;font-size:9px;font-weight:700;margin-bottom:10px;position:relative}
.q::after{content:"+";position:absolute;right:12px;top:7px;font-size:12px}
.q.open{background:var(--yellow);border-color:var(--yellow)}
.q.open::after{content:"–"}
.answer{background:#fff8d8;font-size:9px;color:var(--grey);padding:10px 12px;margin:-10px 0 10px;font-weight:400}
.blog{position:absolute;left:608px;top:50px;width:370px}
.posts{display:grid;grid-template-columns:1fr 1fr;gap:16px}
.post .img{height:120px;background:linear-gradient(135deg,#dcdcdc,#9c9c9c);position:relative}
.post .date{position:absolute;left:8px;top:8px;background:var(--yellow);width:34px;height:34px;font-size:9px;font-weight:700;text-align:center;line-height:1.1;padding-top:5px}
.post h4{font-size:11px;margin:10px 0 6px;line-height:1.3}
.post p{font-size:9px;color:var(--grey)}
.post a{display:block;margin-top:8px;font-size:9px;font-weight:700;color:var(--ink);text-decoration:none}
.site-footer{top:3440px;height:240px;background:var(--darker);color:#bdbdbd;font-size:9px}
.fcols{position:absolute;left:232px;top:40px;width:736px;display:grid;grid-template-columns:190px 150px 150px 200px;gap:16px}
.fcols h4{color:var(--white);font-size:11px;margin-bottom:10px}
.fcols li{list-style:none;margin-bottom:4px}
.fcols .brand .name{color:var(--yellow);font-size:15px}
.fcols .ci{display:flex;gap:8px;margin-bottom:10px}
.bottom{position:absolute;left:0;width:1200px;top:3680px;height:44px;background:#0e0e0f;color:#9a9a9a;font-size:8.5px;display:flex;align-items:center;justify-content:space-between;padding:0 232px}
.bottom .soc{display:flex;gap:6px}
.bottom .soc i{width:18px;height:18px;border-radius:50%;background:#3a3a3a}
</style>
</head>
<body>

<div class="topbar">
  <span>Ductless Experts with 20+ years of experience</span>
  <span class="info"><span>100 Example Lane, Sampletown</span><span>Available Hours: Mon - Sat: 8am - 6pm</span></span>
</div>

<header class="site-header">
  <div class="brand-block">
    <div class="brand"><span class="mark"></span><span class="name">Amber Kite</span></div>
    <div class="sub">DUCTLESS EXPERTS</div>
  </div>
  <div class="header-right">
    <div class="call">
      <svg width="22" height="22" viewBox="0 0 24 24"><path fill="#e2b300" d="M6.6 10.8a15 15 0 0 0 6.6 6.6l2.2-2.2c.3-.3.7-.4 1-.2 1.1.4 2.3.6 3.6.6.6 0 1 .4 1 1V20c0 .6-.4 1-1 1A17 17 0 0 1 3 4c0-.6.4-1 1-1h3.5c.6 0 1 .4 1 1 0 1.3.2 2.5.6 3.6.1.3 0 .7-.2 1z"/></svg>
      <div><small>Call Us Today</small><strong>555-014-3270</strong></div>
    </div>
    <span class="btn">Schedule an Appointment</span>
  </div>
</header>

<nav class="main-nav">
  <a class="active">HOME</a><a>ABOUT US</a><a>DUCTLESS HEAT PUMPS</a><a>DUCTLESS HEAT PUMP FAQ</a><a>FINANCING</a><a>REVIEWS</a><a>CONTACT US</a>
</nav>

<section class="hero">
  <div class="ph photo" role="img" aria-label="Smiling man relaxing on a sofa under a wall-mounted ductless unit"></div>
  <span class="arrow" style="left:10px"></span><span class="arrow" style="right:10px"></span>
  <div class="copy">
    <em>Quality that is Guaranteed</em>
    <h1>Expert Repair Ac &amp; Heating Services</h1>
    <span class="btn">Get a Free Quote</span>
  </div>
</section>

<section class="about">
  <div class="ph photo" role="img" aria-label="Technician in a hard hat servicing an outdoor heat pump"></div>
  <div class="badge">
    <div class="art" role="img" aria-label="Mascot illustration"></div>
    <h3>Amber Kite</h3>
    <p class="sub">Ductless Champion</p>
    <div class="play">
      <span class="c"><svg width="12" height="12" viewBox="0 0 12 12"><path d="M3 1l8 5-8 5z" fill="#f9c80e"/></svg></span>
      <span>Watch Video &amp;<br>Know How We Work</span>
    </div>
  </div>
  <div class="text">
    <p>Ductless mini splits give every room its own comfort. Our team explains each step, from choosing the right size to placing the indoor heads, so you know exactly what you are getting before any work begins.</p>
    <p>We have installed systems in homes, offices and workshops across the region, and we treat every job like it is our own house.</p>
    <h2>Amber Kite Ductless Heroes</h2>
    <p>Our certified installers handle heat pump design, installation, repair and upkeep. We check your space, measure heat loss and recommend a setup that keeps energy bills low all year long.</p>
    <p>Every install is backed by clear pricing, tidy work and friendly follow-up. If something is not right, we come back and make it right, no questions asked.</p>
    <p>Learn how ductless systems work, what they cost and why so many homeowners are making the switch.</p>
  </div>
</section>

<section class="services">
  <div class="section-icon"></div>
  <h2 class="section-title">How Can We Help You?</h2>
  <div class="grid">
    <div class="card"><div class="img" role="img" aria-label="Indoor wall unit"></div><div class="label">Ductless Heat Pump Replacement</div></div>
    <div class="card"><div class="img" role="img" aria-label="Installer fitting a unit"></div><div class="label">Ductless Pump Installation &amp; Services</div></div>
    <div class="card"><div class="img" role="img" aria-label="Outdoor compressor"></div><div class="label">Multi-Zone Heat Pump Systems</div></div>
    <div class="card"><div class="img" role="img" aria-label="Ductless unit on a wall"></div><div class="label">Ductless Installation</div></div>
    <div class="card"><div class="img" role="img" aria-label="Technician cleaning a unit"></div><div class="label">Ductless Maintenance</div></div>
    <div class="card"><div class="img" role="img" aria-label="Technician repairing a unit"></div><div class="label">Ductless Repair</div></div>
    <div class="card"><div class="img" role="img" aria-label="Remote control and unit"></div><div class="label">Ductless Warranty</div></div>
    <div class="card"><div class="img" role="img" aria-label="Bright living room"></div><div class="label">Indoor Air Quality</div></div>
  </div>
  <span class="btn">View Ductless Services</span>
</section>

<section class="contact">
  <div class="section-icon"></div>
  <h2>Contact Us Today</h2>
  <p class="lead">Fill Out The Form Below</p>
  <p class="lead2">(or) Call Amber Kite Ductless Heroes @ <b>555-014-3270</b></p>
  <div class="form">
    <div class="field">First Name</div><div class="field">Last Name</div>
    <div class="field">Email</div><div class="field">Phone</div>
    <div class="field full">Select a Service</div>
    <div class="field full msg">Message</div>
  </div>
  <span class="btn">Send Information</span>
</section>

<section class="reviews">
  <div class="ph photo" role="img" aria-label="Woman enjoying cool air at home"></div>
  <div class="head"><div class="section-icon"></div><h2 class="section-title">Our Customers are Saying About</h2></div>
  <div class="rv" style="left:232px"><div class="box">The crew arrived on time, explained every option and left the house spotless. Our new system is quiet and the bedrooms finally stay cool.<div class="stars">★★★★★</div></div><div class="who">Dana Reyes<span class="av"></span></div></div>
  <div class="rv" style="left:461px"><div class="box">Fair price, quick install and great advice on where to place the units. Our heating bill dropped in the first month. Highly recommended.<div class="stars">★★★★★</div></div><div class="who">Marco Lind<span class="av"></span></div></div>
  <div class="rv" style="left:690px"><div class="box">Friendly people who really know ductless systems. They answered all my questions and followed up after the job was done.<div class="stars">★★★★★</div></div><div class="who">Priya Shah<span class="av"></span></div></div>
  <div class="dots"><i class="on"></i><i></i><i></i><i></i></div>
</section>

<section class="faq-blog">
  <div class="faq">
    <h3>Frequently Asked Questions</h3>
    <div class="q open">1. Is anything required from me before my install?</div>
    <div class="answer">Just clear a path to the rooms and the outdoor area. We bring all parts, mounts and tools, and we walk you through the plan before starting so there are no surprises on the day.</div>
    <div class="q">2. What is a ductless heating and cooling system?</div>
    <div class="q">3. What are the best applications for ductless systems?</div>
    <div class="q">4. How does a ductless system work and why is it so efficient?</div>
    <div class="q">5. Are ductless systems efficient?</div>
  </div>
  <div class="blog">
    <h3>Our Blog</h3>
    <div class="posts">
      <div class="post"><div class="img" role="img" aria-label="Ductless unit in a bedroom"><div class="date">24<br>Dec</div></div><h4>Signs your heat pump needs a tune-up this season</h4><p>Simple checks you can do at home before calling a technician.</p><a>READ MORE</a></div>
      <div class="post"><div class="img" role="img" aria-label="Technician at work"><div class="date">24<br>Dec</div></div><h4>How mini splits cut your monthly energy costs</h4><p>A plain look at zoning, sizing and smart thermostat use.</p><a>READ MORE</a></div>
    </div>
  </div>
</section>

<footer class="site-footer">
  <div class="fcols">
    <div>
      <div class="brand"><span class="mark" style="width:26px;height:26px"></span><span class="name">Amber Kite</span></div>
      <p style="margin-top:10px">Local experts in ductless heating and cooling. We design, install and service mini split systems for homes and small businesses.</p>
    </div>
    <div><h4>QUICK LINKS</h4><ul><li>Home</li><li>About Us</li><li>Ductless Heat Pumps</li><li>Ductless FAQ</li><li>Financing</li><li>Reviews</li></ul></div>
    <div><h4>OTHER LINKS</h4><ul><li>Contact Us</li><li>Service Area</li><li>Privacy Policy</li><li>Site Map</li><li>Blog</li></ul></div>
    <div><h4>CONTACT INFO</h4>
      <div class="ci"><svg width="12" height="12" viewBox="0 0 24 24"><path fill="#f9c80e" d="M12 2a7 7 0 0 0-7 7c0 5 7 13 7 13s7-8 7-13a7 7 0 0 0-7-7zm0 9.5A2.5 2.5 0 1 1 12 6.5a2.5 2.5 0 0 1 0 5z"/></svg><span>100 Example Lane,<br>Sampletown 00000</span></div>
      <div class="ci"><svg width="12" height="12" viewBox="0 0 24 24"><path fill="#f9c80e" d="M6.6 10.8a15 15 0 0 0 6.6 6.6l2.2-2.2c.3-.3.7-.4 1-.2 1.1.4 2.3.6 3.6.6.6 0 1 .4 1 1V20c0 .6-.4 1-1 1A17 17 0 0 1 3 4c0-.6.4-1 1-1h3.5c.6 0 1 .4 1 1 0 1.3.2 2.5.6 3.6.1.3 0 .7-.2 1z"/></svg><span>555-014-3270</span></div>
      <div class="ci"><svg width="12" height="12" viewBox="0 0 24 24"><path fill="#f9c80e" d="M3 5h18v14H3zm2 2v.5l7 5 7-5V7z"/></svg><span>hello@amberkite.example</span></div>
    </div>
  </div>
</footer>
<div class="bottom">
  <span>Copyright © 2024 Amber Kite Services. All Rights Reserved.</span>
  <span class="soc"><i></i><i></i><i></i><i></i></span>
</div>

</body>
</html>
```